Website Design for Law Firm

We need a fresh new website design for our client 'Torvek Legal' who specialises as a Criminal, Traffic & Civil Lawyer in Perth, Western Australia. We are looking for a very clean, professional and elegant look for the website, a presence of power and class needed as he deals with high end clients. Black, Silver and hints of gold need to run through the design without making the site look too dark. We are after a very modern, spacious web look, use of large readable text with links to social media (such as Facebook, Google+, Twitter, LinkedIn) to stand out and his contact details to be made very predominate.

Reason: Public holidays here in Australia, need more business hours to discuss designs with client.

Reason: Client needs more time to look through designs.

Reason: Client is going over last of designs. Design will be picked early next week!

Law Firm

```html
<!DOCTYPE html>
<html lang="en">
<head>
<meta charset="utf-8">
<title>Torvek Legal</title>
<link href="https://fonts.googleapis.com/css2?family=Montserrat:wght@400;500;600&family=Open+Sans:wght@400;600&display=swap" rel="stylesheet">
<style>
:root{
  --gold:#c9a512;
  --gold-dark:#a88a0c;
  --ink:#2a2a2a;
  --charcoal:#1f1f1f;
  --nav:#262626;
  --text:#555;
  --muted:#8a8a8a;
  --paper:#efefef;
  --line:#d9d9d9;
  --white:#fff;
}
*{box-sizing:border-box;margin:0;padding:0}
html,body{width:1200px;height:2635px;overflow:hidden}
body{font-family:"Open Sans",Arial,sans-serif;color:var(--text);background:var(--white);position:relative}
.abs{position:absolute}
h2,h3,h4{font-weight:400}

/* header */
.site-header{position:absolute;left:0;top:0;width:1200px;height:145px;background:linear-gradient(#fff,#f4f4f4);border-top:4px solid var(--gold)}
.brand{position:absolute;left:72px;top:46px;display:flex;align-items:center;gap:10px;font-family:"Montserrat",sans-serif;font-weight:600;font-size:30px;color:var(--ink);letter-spacing:1px;white-space:nowrap}
.brand-mark{width:22px;height:22px;background:var(--ink);flex:none}
.social{position:absolute;left:838px;top:38px;display:flex;gap:8px}
.social span{width:24px;height:24px;border-radius:50%;background:#3a6fb0}
.search{position:absolute;left:945px;top:36px;width:212px;height:31px;border:1px solid #ccc;border-radius:16px;background:#fff;font-size:12px;color:#777;padding:7px 16px}
.search svg{position:absolute;right:12px;top:9px}
.main-nav{position:absolute;left:318px;top:92px;width:882px;height:53px;background:var(--nav);clip-path:polygon(22px 0,100% 0,100% 100%,0 100%);display:flex;align-items:center;padding-left:36px;gap:40px}
.main-nav a{font-family:"Montserrat",sans-serif;font-size:13px;color:#eee;text-decoration:none;letter-spacing:.8px;white-space:nowrap}

/* hero */
.hero{position:absolute;left:0;top:145px;width:1200px;height:475px;background:linear-gradient(100deg,#d9e0dd 0%,#b8c2c0 35%,#5d6670 55%,#cfd8d5 80%,#e3e9e6 100%)}
.case-form{position:absolute;left:783px;top:188px;width:334px;height:380px;background:#2c2c2c;clip-path:polygon(0 0,100% 0,100% 340px,50% 100%,0 340px)}
.case-form h2{height:44px;background:linear-gradient(#d8b51f,var(--gold-dark));color:#fff;font-family:"Montserrat",sans-serif;font-weight:500;font-size:20px;letter-spacing:1px;text-align:center;line-height:44px}
.field{position:absolute;background:#fff;border-radius:3px;font-size:12px;color:#888;padding:6px 10px;height:30px}
.submit{position:absolute;left:75px;top:286px;width:184px;height:40px;background:linear-gradient(#e0bd26,var(--gold-dark));border-radius:3px;color:#fff;font-family:"Montserrat",sans-serif;font-size:16px;text-align:center;line-height:40px;letter-spacing:1px}

/* practice areas */
.practice{position:absolute;left:0;top:620px;width:1200px;height:678px;background:var(--paper)}
.section-title{font-family:"Montserrat",sans-serif;font-weight:400;font-size:21px;color:var(--ink);letter-spacing:1px;white-space:nowrap}
.section-title em{font-style:normal;color:var(--gold)}
.area{position:absolute;width:600px;height:228px}
.area h3{position:absolute;left:228px;top:119px;font-family:"Montserrat",sans-serif;font-weight:500;font-size:17px;color:var(--ink);letter-spacing:1px}
.area p{position:absolute;left:228px;top:146px;width:330px;font-size:14px;line-height:20px;color:#666}
.area .more{color:var(--gold);font-size:13px}
.area svg{position:absolute;left:70px;top:100px}
.grid-line-v{position:absolute;left:599px;top:708px;width:1px;height:456px;background:var(--line)}
.grid-line-h{position:absolute;left:45px;top:930px;width:1110px;height:1px;background:var(--line)}
.view-all{position:absolute;left:510px;top:1188px;width:180px;height:42px;background:var(--nav);border-bottom:3px solid var(--gold);color:#fff;font-family:"Montserrat",sans-serif;font-size:15px;letter-spacing:1px;text-align:center;line-height:40px}

/* welcome & cases */
.welcome-text{position:absolute;left:88px;top:1430px;width:470px;font-size:14px;line-height:23px;color:#555}
.welcome-text p{margin-bottom:23px}
.rule{position:absolute;height:1px;background:#ccc}
.read-more{position:absolute;left:84px;top:1771px;width:138px;height:34px;background:var(--nav);border-bottom:3px solid var(--gold);color:#fff;font-size:13px;text-align:center;line-height:31px}
.case{position:absolute;left:648px;width:460px;height:90px}
.case .thumb{position:absolute;left:0;top:0;width:128px;height:84px;border:3px solid #ddd}
.case h4{position:absolute;left:138px;top:-2px;font-family:"Open Sans",sans-serif;font-weight:400;font-size:16px;color:#333}
.case p{position:absolute;left:138px;top:22px;width:325px;font-size:13px;line-height:19px;color:#666}

/* map */
.map{position:absolute;left:0;top:1862px;width:1200px;height:313px;background:linear-gradient(120deg,#e6e2d8,#ded9cd 50%,#e4e0d6)}

/* newsletter */
.newsletter{position:absolute;left:0;top:2175px;width:1200px;height:105px;background:linear-gradient(#3a3a3a,#262626)}
.newsletter .brand{left:112px;top:40px;gap:8px;color:#eee;font-size:20px;letter-spacing:.5px}
.newsletter .brand-mark{width:16px;height:16px;background:#eee}
.news-input{position:absolute;left:300px;top:33px;width:648px;height:42px;background:#fff;border-radius:2px;font-size:15px;color:#999;padding:11px 16px;letter-spacing:.5px}
.news-btn{position:absolute;left:956px;top:33px;width:148px;height:44px;background:#1b1b1b;border-bottom:3px solid var(--gold);color:#fff;font-family:"Montserrat",sans-serif;font-size:13px;text-align:center;line-height:42px;letter-spacing:.8px}

/* footer */
.site-footer{position:absolute;left:0;top:2280px;width:1200px;height:312px;background:linear-gradient(#343434,#232323)}
.foot-title{position:absolute;top:60px;font-family:"Montserrat",sans-serif;font-weight:500;font-size:15px;color:#eee;letter-spacing:1px;white-space:nowrap}
.foot-rule{position:absolute;top:90px;height:1px;background:#555}
.foot-links{position:absolute;top:106px;list-style:none;font-size:12.5px;line-height:24px;color:#ddd;letter-spacing:.5px}
.foot-social{position:absolute;left:106px;top:211px;display:flex;gap:6px}
.foot-social span{width:22px;height:22px;border-radius:50%;background:#f2f2f2}
.card{position:absolute;top:2412px;width:82px;height:52px;background:#fafafa;border-radius:5px;font-family:"Montserrat",sans-serif;font-size:13px;font-weight:500;color:#333;text-align:center;line-height:52px}
.cards-note{position:absolute;left:768px;top:2490px;width:340px;text-align:center;font-size:10px;color:#ccc;letter-spacing:.8px;font-family:"Montserrat",sans-serif}
.copyright{position:absolute;left:0;top:2592px;width:1200px;height:43px;background:#141414;color:#ddd;font-size:13px;text-align:center;line-height:43px}
</style>
</head>
<body>

<header class="site-header">
  <div class="brand"><span class="brand-mark"></span>Torvek Legal</div>
  <div class="social" aria-label="Social links"><span></span><span style="background:#3aa3d8"></span><span style="background:#2a76b0"></span></div>
  <div class="search">Keyword Search
    <svg width="12" height="12" viewBox="0 0 12 12"><circle cx="5" cy="5" r="3.6" fill="none" stroke="#999" stroke-width="1.5"/><line x1="7.6" y1="7.6" x2="11" y2="11" stroke="#999" stroke-width="1.5"/></svg>
  </div>
  <nav class="main-nav">
    <a href="#">HOME</a><a href="#">ABOUT US</a><a href="#">PRACTICE AREAS</a><a href="#">SCOPE OF ADVICE</a><a href="#">LEGAL COST</a><a href="#">PRESS</a><a href="#">CONTACT</a>
  </nav>
</header>

<section class="hero" role="img" aria-label="Photo of a senior lawyer in a suit standing in front of his legal team"></section>
<form class="case-form">
  <h2>• Free Case Assesment •</h2>
  <div class="field" style="left:18px;top:76px;width:144px">Firstname</div>
  <div class="field" style="left:172px;top:76px;width:144px">Lastname</div>
  <div class="field" style="left:18px;top:119px;width:144px">Phone no.</div>
  <div class="field" style="left:172px;top:119px;width:144px">Email</div>
  <div class="field" style="left:18px;top:164px;width:298px;height:102px">Message...</div>
  <div class="submit">SUBMIT</div>
</form>

<section class="practice">
  <h2 class="section-title abs" style="left:0;width:1200px;text-align:center;top:26px">PRACTICE <em>AREAS</em></h2>
</section>
<div class="grid-line-v"></div>
<div class="grid-line-h"></div>

<div class="area" style="left:0;top:620px">
  <svg width="120" height="100" viewBox="0 0 120 100"><g fill="none" stroke="var(--gold)" stroke-width="9"><circle cx="32" cy="40" r="22"/><circle cx="86" cy="60" r="22"/><path d="M50 30 Q60 22 70 44"/></g></svg>
  <h3>CRIMINAL LAW</h3>
  <p>Lorem ipsum dolor sit amet, consectetur adipiscing elit. Fusce vestibulum dui vitae tincidunt, a placerat ipsum feugiat. Aliquam adipiscing consectetur tellus interdum ui vitae tincidunt a placerat.<br><span class="more">Read more ›</span></p>
</div>
<div class="area" style="left:567px;top:620px">
  <svg width="120" height="110" viewBox="0 0 120 110"><g fill="var(--gold)"><rect x="56" y="8" width="8" height="80"/><rect x="10" y="24" width="100" height="6"/><rect x="36" y="88" width="48" height="12" rx="3"/><path d="M6 60 h40 a20 12 0 0 1 -40 0z"/><path d="M74 60 h40 a20 12 0 0 1 -40 0z"/></g><g stroke="var(--gold)" stroke-width="2"><path d="M14 30 L6 60 M14 30 L46 60 M106 30 L74 60 M106 30 L114 60"/></g></svg>
  <h3>CIVIL LAW</h3>
  <p>Lorem ipsum dolor sit amet, consectetur adipiscing elit. Fusce vestibulum dui vitae tincidunt, a placerat ipsum feugiat. Aliquam adipiscing consectetur tellus interdum ui vitae tincidunt a placerat.<br><span class="more">Read more ›</span></p>
</div>
<div class="area" style="left:0;top:848px">
  <svg width="120" height="110" viewBox="0 0 120 110"><rect x="38" y="4" width="44" height="100" rx="8" fill="var(--gold)"/><g fill="#8a7208"><circle cx="60" cy="26" r="10"/><circle cx="60" cy="54" r="10"/><circle cx="60" cy="82" r="10"/></g></svg>
  <h3>TRAFFIC LAW</h3>
  <p>Lorem ipsum dolor sit amet, consectetur adipiscing elit. Fusce vestibulum dui vitae tincidunt, a placerat ipsum feugiat. Aliquam adipiscing consectetur tellus interdum ui vitae tincidunt a placerat.<br><span class="more">Read more ›</span></p>
</div>
<div class="area" style="left:567px;top:848px">
  <svg width="120" height="110" viewBox="0 0 120 110"><g fill="var(--gold)"><path d="M60 2 L114 28 H6z"/><rect x="10" y="32" width="100" height="7"/><rect x="18" y="44" width="12" height="46"/><rect x="40" y="44" width="12" height="46"/><rect x="68" y="44" width="12" height="46"/><rect x="90" y="44" width="12" height="46"/><rect x="6" y="94" width="108" height="12"/></g></svg>
  <h3>COURT WORK</h3>
  <p>Lorem ipsum dolor sit amet, consectetur adipiscing elit. Fusce vestibulum dui vitae tincidunt, a placerat ipsum feugiat. Aliquam adipiscing consectetur tellus interdum ui vitae tincidunt a placerat.<br><span class="more">Read more ›</span></p>
</div>
<div class="view-all">VIEW ALL</div>

<h2 class="section-title abs" style="left:86px;top:1354px">WELCOME TO <em>TORVEK LEGAL</em></h2>
<div class="rule" style="left:86px;top:1404px;width:476px"></div>
<div class="welcome-text">
  <p>Torvek Legal is an established Law firm specialising in Criminal Law, Traffic Law and Civil Law. Dr Elias Torvek is the firm's Legal Practitioner Director.</p>
  <p>Elias is an experienced Legal Advocate dedicated to protecting you legal rights.</p>
  <p>In the last two years he has notched up over 2,000 appearances in the Magistrates Court, District Court, Supreme Court and Children's Court.</p>
  <p>Elias was formerly with the Public Defence Office of WA Criminal Division and before that he enjoyed a long and successful international career with various agencies of the Global Justice Council. He has taught Criminal Law and Advanced Criminal Law</p>
</div>
<div class="read-more">Read more</div>

<h2 class="section-title abs" style="left:644px;top:1354px">RECENT <em>CASES</em></h2>
<div class="rule" style="left:644px;top:1404px;width:466px"></div>
<div class="case" style="top:1426px">
  <div class="thumb" role="img" aria-label="Photo of a business handshake" style="background:linear-gradient(135deg,#2b2f36,#6c7077)"></div>
  <h4>Article Title goes here</h4>
  <p>Lorem ipsum dolor sit amet, consectetur adipiscing elit. Phasellus eget leo leo. Sed adipiscing mi orci, vel ultrices turpis mattis a.</p>
</div>
<div class="case" style="top:1543px">
  <div class="thumb" role="img" aria-label="Photo of a judge's gavel on banknotes" style="background:linear-gradient(135deg,#4a2a14,#b6894c)"></div>
  <h4>Article Title goes here</h4>
  <p>Lorem ipsum dolor sit amet, consectetur adipiscing elit. Phasellus eget leo leo. Sed adipiscing mi orci, vel ultrices turpis mattis a.</p>
</div>
<div class="case" style="top:1660px">
  <div class="thumb" role="img" aria-label="Photo of a hand signing a document" style="background:linear-gradient(135deg,#3e2a1c,#c7a57a)"></div>
  <h4>Article Title goes here</h4>
  <p>Lorem ipsum dolor sit amet, consectetur adipiscing elit. Phasellus eget leo leo. Sed adipiscing mi orci, vel ultrices turpis mattis a.</p>
</div>

<section class="map" role="img" aria-label="Street map of central Perth with the office location marked"></section>

<section class="newsletter">
  <div class="brand"><span class="brand-mark"></span>Torvek Legal</div>
  <div class="news-input">Send us your Email to Join our monthly Newsletter</div>
  <div class="news-btn">SUBSCRIBE</div>
</section>

<footer class="site-footer">
  <h3 class="foot-title" style="left:100px">QUICKLINKS</h3>
  <div class="foot-rule" style="left:100px;width:248px"></div>
  <ul class="foot-links" style="left:106px"><li>Home</li><li>About</li><li>Practice Areas</li><li>Scope of Advice</li></ul>
  <ul class="foot-links" style="left:246px"><li>Legal Cost</li><li>Recent Cases</li><li>Press</li><li>Contact</li></ul>
  <div class="foot-social" aria-label="Social links"><span></span><span></span><span></span><span></span></div>
  <h3 class="foot-title" style="left:456px">USEFUL INFORMATION</h3>
  <div class="foot-rule" style="left:456px;width:214px"></div>
  <ul class="foot-links" style="left:463px"><li>Sitemap</li><li>F.A.Q</li><li>Service Policy</li><li>Terms &amp; Conditions</li></ul>
  <h3 class="foot-title" style="left:768px">FOR YOUR CONVENIECE WE ACCEPT:</h3>
  <div class="foot-rule" style="left:768px;width:348px"></div>
</footer>
<div class="card" style="left:788px">Cardora</div>
<div class="card" style="left:899px">Paylex</div>
<div class="card" style="left:1010px">Tapnet</div>
<div class="cards-note">ALL MAJOR CREDIT CARDS ARE ACCEPTED</div>
<div class="copyright">Copyright 2014 &nbsp;All rights reserved</div>

</body>
</html>
```